MENSTRUATION

Website Design Brief
*Note: I am also a professional graphic designer, so please make a note of that and present your best work. If you are not a professional graphic designer, please do not post anything or invest time.
Project Title: Menstruation Education & Support Website for Teens and Parents
________________________________________
1. Project Overview
We aim to create an engaging, educational, and supportive online platform dedicated to menstruation awareness and guidance.
The website will serve two primary audiences:
1. Teens aged 13–16
o Objective: Educate and empower them with knowledge about menstruation, menstrual health, hygiene, and emotional well-being.
o Tone: Playful, approachable, friendly, and relatable.
2. Parents/Women
o Objective: Provide in-depth resources, support communities, and expert advice to help them support their teens (or themselves) through menstruation-related challenges.
o Tone: Serious, mature, trustworthy, and empathetic.
The website will be dual-themed to cater to each audience’s emotional and visual expectations while maintaining a unified brand identity.
2. Goals & Objectives
• Educate teens in a fun and approachable way about menstruation.
• Provide safe spaces for open discussion, both for teens and for parents.
• Encourage intergenerational conversation between parents and teens.
• Destigmatize menstruation through positive, engaging design and language.
• Offer credible information backed by health professionals.
3. Target Audiences
• Primary Teen Audience (13–16 years old):
o Tech-savvy, visually driven, short attention spans.
o Need reassurance, relatability, and accurate information.
• Primary Parent/Women Audience:
o Concerned with their children’s well-being.
o Seeking practical advice, medical information, and a supportive community.
4. Website Structure & Sections
A. Teen Section ("Playful & Cute Look")
• Design Style:
o Bright pastel colors (pink, lavender, sky blue, mint).
o Whimsical illustrations (Lumvic/Korrin-like characters, friendly mascots).
o Sparkles, soft shapes, rounded edges, playful animations.
• Features:
o Educational Guides – Menstrual cycle basics, hygiene tips, dealing with cramps, myths & facts.
o Interactive Period Tracker – Cute UI, gamified elements.
o Ask an Expert – Anonymous Q&A with professionals.
o Story Corner – Real teen stories about first periods.
o Fun Zone – Quizzes, mood trackers, self-care tips.
B. Parent/Women Section ("Serious & Mature Look")
• Design Style:
o Neutral and warm tones (earthy beige, soft gray, deep burgundy).
o Clean layouts, minimalistic icons, serif fonts for elegance.
o Subtle animations for professionalism.
• Features:
o Expert Articles – Menstrual health, nutrition, emotional support.
o Parenting Tips – Helping teens manage periods with confidence.
o Discussion Forum – Moderated safe space for parents/women to share experiences.
o Medical Resources – Links to reputable health organizations.
o Downloadable Guides – Printable resources for home use.
C. Shared/Bridging Content (Unified Brand Tone)
• About Us – Mission, vision, credibility.
• Health Professional Endorsements – Bios of medical advisors.
• Contact & Support – Email, live chat, helpdesk.
• Language Toggle – Option for multiple languages.
• Accessibility Features – Dyslexia-friendly fonts, text resizing, high contrast mode.
5. Navigation
• Dual-Entry Landing Page
o Upon visiting, users choose: "For Teens" or "For Parents/Women".
o Each section retains its design style but keeps consistent logo and branding.
6. Technical Requirements
• Responsive Design – Works seamlessly on mobile, tablet, and desktop.
• Secure Login – For community areas (with parental consent for minors).
• Moderation Tools – AI-assisted and human moderation to ensure safety.
• SEO Optimization – For health-related keyword ranking.
• CMS – Easy content updates for articles and resources.
7. Additional Creative Ideas
• Mascot Character – A friendly animated character guiding teens through content.
• Parent-Teen Joint Activities Section – Fun bonding ideas related to menstrual health education.
• Myth-Busting Series – Quick animated videos addressing common menstrual myths.
• Interactive Body Map – Clickable diagram explaining reproductive anatomy in a simple way.
• Monthly Newsletter – Separate teen and parent editions.
• Private Journaling Feature – Teens can log moods, symptoms, and notes.
8. Brand Personality
• For Teens: Friendly, encouraging, sparkly, non-judgmental, empowering.
• For Parents: Respectful, informative, empathetic, trustworthy.
9. Deliverables Expected from Designers
• Wireframes for both sections.
• Complete UI/UX design with separate visual themes for each audience.
• Branding package (color palettes, typography, illustration style).
• Icons & graphics consistent with each section’s theme.
• Guidelines for animations and transitions.
For the teens section something Lumvic-like or Korrin-like could also be interesting.
Please note that I am a professional graphic designer so please only spend time doing a design that you
truly feel is awesome and professional, otherwise it will just be a waste of time. Doing drafts with chatgpt will not work, I've seen them all.
thanks
1 page

```html
<!DOCTYPE html>
<html lang="en">
<head>
<meta charset="UTF-8">
<title>Menstruation — Choose Your Path</title>
<link rel="stylesheet" href="https://fonts.googleapis.com/css2?family=DM+Sans:wght@600;700&family=Roboto:wght@400&display=swap">
<style>
  :root {
    --teal: #34b4bf;
    --teal-deep: #2a9fab;
    --purple: #9158c6;
    --purple-deep: #6d34a4;
    --white: #ffffff;
    --footer-bg: #ffffff;
    --footer-text: #444444;
  }
  * { margin: 0; padding: 0; box-sizing: border-box; }
  html, body { width: 1200px; height: 780px; overflow: hidden; }
  body { position: relative; background: var(--footer-bg); font-family: "DM Sans", sans-serif; }

  .landing-hero { position: absolute; left: 0; top: 0; width: 1200px; height: 714px; overflow: hidden; }
  .teen-photo {
    position: absolute; inset: 0;
    background: radial-gradient(ellipse at 30% 40%, #3fc0ca 0%, var(--teal) 45%, var(--teal-deep) 100%);
  }
  .women-photo { position: absolute; inset: 0; width: 1200px; height: 714px; }

  .site-title {
    position: absolute; top: 44px; left: 0; width: 1200px;
    text-align: center; color: var(--white);
    font-weight: 600; font-size: 70px; letter-spacing: 0.5px; line-height: 1;
  }

  .audience-entry { position: absolute; text-decoration: none; color: var(--white); }
  .audience-icon { position: absolute; }
  .audience-label {
    position: absolute; border-top: 1.5px solid var(--white); border-bottom: 1.5px solid var(--white);
    text-align: center; font-weight: 600; font-size: 44px; line-height: 66px; letter-spacing: 0.3px;
  }
  .entry-teens .audience-icon { left: 237px; top: 240px; }
  .entry-teens .audience-label { left: 189px; top: 379px; width: 225px; height: 70px; }
  .entry-women .audience-icon { left: 828px; top: 248px; }
  .entry-women .audience-label { left: 748px; top: 381px; width: 273px; height: 70px; }

  .site-footer {
    position: absolute; left: 0; top: 714px; width: 1200px; height: 66px;
    display: flex; align-items: center; justify-content: center;
    font-family: "Roboto", sans-serif; font-size: 16px; color: var(--footer-text);
  }
</style>
</head>
<body>
  <main class="landing-hero">
    <div class="teen-photo" role="img" aria-label="Photo of a smiling group of teenage friends taking a selfie, tinted teal"></div>
    <svg class="women-photo" viewBox="0 0 1200 714" role="img" aria-label="Photo of a smiling young woman with a headscarf, tinted purple">
      <defs>
        <linearGradient id="womenTint" x1="0" y1="0" x2="1" y2="1">
          <stop offset="0" stop-color="#9a62cc"/>
          <stop offset="0.55" stop-color="var(--purple)"/>
          <stop offset="1" stop-color="var(--purple-deep)"/>
        </linearGradient>
      </defs>
      <path d="M776,0 C620,130 530,330 534,470 C536,560 556,640 584,714 L1200,714 L1200,0 Z" fill="url(#womenTint)"/>
    </svg>

    <h1 class="site-title">Menstruation</h1>

    <a class="audience-entry entry-teens" href="#teens">
      <svg class="audience-icon" width="124" height="118" viewBox="0 0 124 118" fill="none" stroke="#fff" stroke-width="1.5" stroke-linejoin="round" stroke-linecap="round">
        <path d="M6,1 H117 A5,5 0 0 1 122,6 V96 A5,5 0 0 1 117,101 H73 L61,113 L49,101 H6 A5,5 0 0 1 1,96 V6 A5,5 0 0 1 6,1 Z"/>
        <circle cx="61.5" cy="45" r="13"/>
        <path d="M39,80 C39,66 48,61 61.5,61 C75,61 84,66 84,80"/>
      </svg>
      <div class="audience-label">For Teens</div>
    </a>

    <a class="audience-entry entry-women" href="#women">
      <svg class="audience-icon" width="124" height="118" viewBox="0 0 124 118" fill="none" stroke="#fff" stroke-width="1.5" stroke-linejoin="round" stroke-linecap="round">
        <path d="M6,1 H117 A5,5 0 0 1 122,6 V96 A5,5 0 0 1 117,101 H73 L61,113 L49,101 H6 A5,5 0 0 1 1,96 V6 A5,5 0 0 1 6,1 Z"/>
        <circle cx="61.5" cy="41" r="14"/>
        <path d="M39,83 C39,68 48,63 61.5,63 C75,63 84,68 84,83"/>
        <path d="M54,64 L61.5,76 L69,64"/>
      </svg>
      <div class="audience-label">For Womens</div>
    </a>
  </main>

  <footer class="site-footer">© 2025 Company Name | All Rights Reserved</footer>
</body>
</html>
```